Bref créative
Bellwether Rheumatology Associates
The Institute for Bone Density
I need double sided standard sized Business Card [3.5" x 2"]
We are flexible, can use different font if looks good.
Professional
Daniel P. Hurlow, MD
Harborview Lakes Medical Center
2716 Kelmont Avenue, Suite 430
Miami Beach, FL 33187
dhurlow1982@mailbrook.example
We are presently a group of two rheumatologists. We are expecting a third rheumatologist the summer of 2012. We will need two versions, one that has my name, Daniel P. Hurlow, MD, and the other that has my partner's name Tomas L. Ferreira Vidal, MD. We are striving for a modern, clean, professional, corporate look. Please use the logo that we are providing. Will be uploading. Would like to keep colors simple. As per logo, we use dark red and gray; I suppose the text on the card will need to be black or similar. Please do NOT put email on card. We still do not have an "official" email. Will also like to see letterhead and envelope design, as well. With the envelope, we are simply looking for a neat-looking, recognizable return address section.
The back of the business card should be the appointment reminder section. Should have a blank for 1. Patient name, 2. Date of appointment 3. Time of appointment 4. Day of week that we can circle (mon-fri only) 5. check box for doctor (either Daniel P. Hurlow, MD or Tomas L. Ferreira Vidal).
Here is the logo.

```html
<!DOCTYPE html>
<html lang="en">
<head>
<meta charset="utf-8">
<title>Bellwether Rheumatology Associates – Stationery</title>
<link rel="stylesheet" href="https://fonts.googleapis.com/css2?family=Libre+Baskerville:wght@700&family=Arimo:wght@400;700&display=swap">
<style>
:root{
  --bg:#1c1c1c;
  --paper:#ffffff;
  --brand-red:#8c1c22;
  --ink:#1e1e1e;
  --grey:#6d6d6d;
  --line:#b9b9b9;
  --shadow:rgba(0,0,0,.55);
}
*{box-sizing:border-box;margin:0;padding:0}
html,body{width:1200px;height:643px;overflow:hidden;background:var(--bg)}
body{position:relative;font-family:"Arimo",Arial,sans-serif;color:var(--ink)}
.sheet{position:absolute;background:var(--paper);box-shadow:0 4px 14px var(--shadow);overflow:hidden}

/* brand lockup */
.brand{display:flex;align-items:center;gap:5px}
.brand-mark{width:12px;height:12px;background:var(--brand-red);flex:none}
.brand-name{font-family:"Libre Baskerville",Georgia,serif;font-weight:700;color:var(--brand-red);text-transform:uppercase;line-height:1.15;letter-spacing:.02em}

/* business cards */
.business-card{left:24px;width:276px;height:166px}
.business-card.card-hurlow{top:72px}
.business-card.card-ferreira{top:252px}
.business-card .brand{position:absolute;left:12px;top:12px}
.business-card .brand-name{font-size:7.5px;width:170px}
.business-card .card-rule{position:absolute;left:12px;right:12px;top:46px;height:2px;background:var(--brand-red)}
.business-card .card-address{position:absolute;left:12px;bottom:14px;font-size:6.6px;line-height:1.45;color:var(--ink)}
.business-card .card-name{position:absolute;right:12px;top:78px;font-size:8.5px;font-weight:700;text-align:right;max-width:140px}

/* appointment card */
.appointment-card{left:24px;top:432px;width:276px;height:166px;padding:10px 14px}
.appointment-title{color:var(--brand-red);font-size:9px;font-weight:700;text-align:center;margin-bottom:12px}
.field{display:flex;align-items:flex-end;gap:6px;font-size:7px;margin-bottom:9px}
.field .blank{flex:1;border-bottom:1px solid var(--grey);height:8px}
.weekdays{display:flex;gap:8px;margin:4px 0 14px 30px}
.weekday{text-align:center;font-size:6.5px}
.weekday .box{width:24px;height:14px;border:1px solid var(--grey);margin-top:2px}
.doctor-options{display:flex;justify-content:space-between;font-size:6.5px}
.doctor-option{display:flex;align-items:center;gap:4px}
.doctor-option .check{width:8px;height:8px;border:1px solid var(--grey)}

/* letterhead */
.letterhead{left:331px;top:48px;width:485px;height:552px;padding:22px 30px}
.letterhead .brand .brand-mark{width:16px;height:16px}
.letterhead .brand-name{font-size:9.5px;width:200px}
.letterhead-contact{position:absolute;right:30px;top:24px;font-size:6.2px;line-height:1.45;text-align:left;color:var(--ink)}
.letter{margin-top:34px;font-size:6.4px;line-height:1.5;color:var(--ink)}
.recipient{margin-bottom:22px}
.salutation{margin-bottom:10px}
.letter p.body{margin-bottom:10px;text-align:justify}
.closing{margin-top:18px}
.signature{width:70px;height:22px;margin:8px 0 4px;background:linear-gradient(90deg,#d7dbe6,#c3c9da)}
.letterhead-footer{position:absolute;left:30px;right:30px;bottom:14px;height:2px;background:var(--brand-red)}

/* envelopes */
.envelope{left:852px;width:336px;height:168px}
.envelope-back{top:240px;background:#f4f4f4}
.envelope-back svg{position:absolute;inset:0}
.envelope-front{top:420px}
.envelope-front .brand{position:absolute;left:14px;top:14px}
.envelope-front .brand-name{font-size:7.5px;width:170px}
.return-address{position:absolute;left:31px;top:46px;font-size:6px;line-height:1.45}
</style>
</head>
<body>

<!-- business card: Hurlow -->
<section class="sheet business-card card-hurlow">
  <div class="brand"><span class="brand-mark"></span><span class="brand-name">Bellwether Rheumatology Associates<br>The Institute for Bone Density</span></div>
  <div class="card-rule"></div>
  <div class="card-name">Daniel P. Hurlow, MD</div>
  <address class="card-address" style="font-style:normal">
    Harborview Lakes Medical Center<br>
    2716 Kelmont Avenue, Suite 430<br>
    Miami Beach, FL 33187<br>
    T &nbsp;(305) 555-0142<br>
    F &nbsp;(305) 555-0187
  </address>
</section>

<!-- business card: Ferreira Vidal -->
<section class="sheet business-card card-ferreira">
  <div class="brand"><span class="brand-mark"></span><span class="brand-name">Bellwether Rheumatology Associates<br>The Institute for Bone Density</span></div>
  <div class="card-rule"></div>
  <div class="card-name">Tomas L. Ferreira Vidal, MD</div>
  <address class="card-address" style="font-style:normal">
    Harborview Lakes Medical Center<br>
    2716 Kelmont Avenue, Suite 430<br>
    Miami Beach, FL 33187<br>
    T &nbsp;(305) 555-0142<br>
    F &nbsp;(305) 555-0187
  </address>
</section>

<!-- appointment reminder (card back) -->
<section class="sheet appointment-card">
  <h2 class="appointment-title">My Next Appointment</h2>
  <div class="field"><span>Patient Name:</span><span class="blank"></span></div>
  <div class="field"><span>Date:</span><span class="blank"></span><span>Time:</span><span class="blank"></span></div>
  <div class="weekdays">
    <div class="weekday">Mon<div class="box"></div></div>
    <div class="weekday">Tue<div class="box"></div></div>
    <div class="weekday">Wed<div class="box"></div></div>
    <div class="weekday">Thu<div class="box"></div></div>
    <div class="weekday">Fri<div class="box"></div></div>
  </div>
  <div class="doctor-options">
    <span class="doctor-option"><span class="check"></span>Daniel P. Hurlow, MD</span>
    <span class="doctor-option"><span class="check"></span>Tomas L. Ferreira Vidal, MD</span>
  </div>
</section>

<!-- letterhead -->
<section class="sheet letterhead">
  <div class="brand"><span class="brand-mark"></span><span class="brand-name">Bellwether Rheumatology Associates<br>The Institute for Bone Density</span></div>
  <address class="letterhead-contact" style="font-style:normal">
    Harborview Lakes Medical Center<br>
    2716 Kelmont Avenue, Suite 430<br>
    Miami Beach, FL 33187<br>
    T (305) 555-0142<br>
    F (305) 555-0187
  </address>
  <div class="letter">
    <p class="recipient">Someone Somebody<br>100 Long Street<br>Anytown, FL 00000</p>
    <p class="salutation">Dear Someone Somebody,</p>
    <p class="body">Lorem ipsum dolor sit amet, consectetur adipiscing elit, sed do eiusmod tempor incididunt ut labore et dolore magna aliqua. Ut enim ad minim veniam, quis nostrud exercitation ullamco laboris nisi ut aliquip ex ea commodo consequat. Duis aute irure dolor in reprehenderit in voluptate velit esse cillum dolore.</p>
    <p class="body">Lorem ipsum dolor sit amet, consectetur adipiscing elit, sed do eiusmod tempor incididunt ut labore et dolore magna aliqua. Ut enim ad minim veniam, quis nostrud exercitation ullamco laboris nisi ut aliquip ex ea commodo consequat. Duis aute irure dolor in reprehenderit in voluptate velit esse cillum dolore.</p>
    <p class="body">Lorem ipsum dolor sit amet, consectetur adipiscing elit, sed do eiusmod tempor incididunt ut labore et dolore magna aliqua. Ut enim ad minim veniam, quis nostrud exercitation ullamco laboris nisi ut aliquip ex ea commodo consequat. Duis aute irure dolor in reprehenderit in voluptate velit esse cillum dolore.</p>
    <p class="body">Excepteur sint occaecat cupidatat non proident, sunt in culpa qui officia deserunt mollit anim.</p>
    <p class="closing">Yours Sincerely,<br>Daniel Hurlow</p>
    <div class="signature" role="img" aria-label="Handwritten signature"></div>
  </div>
  <div class="letterhead-footer"></div>
</section>

<!-- envelope back -->
<section class="sheet envelope envelope-back">
  <svg width="336" height="168" viewBox="0 0 336 168">
    <polyline points="0,0 168,78 336,0" fill="#ffffff" stroke="#cfcfcf" stroke-width="1"/>
    <line x1="0" y1="168" x2="140" y2="70" stroke="#dcdcdc" stroke-width="1"/>
    <line x1="336" y1="168" x2="196" y2="70" stroke="#dcdcdc" stroke-width="1"/>
  </svg>
</section>

<!-- envelope front -->
<section class="sheet envelope envelope-front">
  <div class="brand"><span class="brand-mark"></span><span class="brand-name">Bellwether Rheumatology Associates<br>The Institute for Bone Density</span></div>
  <address class="return-address" style="font-style:normal">
    Harborview Lakes Medical Center<br>
    2716 Kelmont Avenue, Suite 430<br>
    Miami Beach, FL 33187
  </address>
</section>

</body>
</html>
```